Business Card Design

I'd like to have some business cards designed using my new logo. I am an accountant and company secretary and offer these services through Holloway Meridian Advisory Pty Ltd. I am the sole Director of the company. Please let me know if you require any further logo files.

Industry/Entity Type

Business

```html
<!DOCTYPE html>
<html lang="en">
<head>
<meta charset="utf-8">
<title>Holloway Meridian Advisory – Business Cards</title>
<link rel="stylesheet" href="https://fonts.googleapis.com/css2?family=Cinzel:wght@400;600&family=Open+Sans:wght@400;600&display=swap">
<style>
  :root {
    --bg: #e9e6e1;
    --card-white: #ffffff;
    --card-black: #1b1a1c;
    --card-black-light: #3a393d;
    --brand-blue: #1a7cc6;
    --brand-blue-light: #4aa3e0;
    --brand-grey: #6d6e72;
    --text-light: #f2f2f2;
    --text-muted: #8a8b90;
  }
  * { margin: 0; padding: 0; box-sizing: border-box; }
  html, body { width: 1200px; height: 1014px; overflow: hidden; }
  body { background: var(--bg); position: relative; font-family: "Open Sans", sans-serif; }

  .card {
    position: absolute;
    width: 540px;
    height: 309px;
    border-radius: 3px;
    overflow: hidden;
    box-shadow: 0 10px 28px rgba(0,0,0,0.28);
  }
  .card--front { left: 60px; top: 150px; background: var(--card-white); }
  .card--back {
    left: 600px; top: 555px;
    background: linear-gradient(135deg, var(--card-black) 0%, var(--card-black-light) 55%, var(--card-black) 100%);
  }
  .card__art { position: absolute; inset: 0; width: 100%; height: 100%; }

  .brand {
    position: absolute;
    display: flex;
    align-items: center;
    gap: 10px;
    white-space: nowrap;
  }
  .brand__dot { width: 22px; height: 22px; border-radius: 50%; background: var(--brand-blue); flex: none; }
  .brand--front { left: 190px; top: 62px; }
  .brand__name {
    font-family: "Open Sans", sans-serif;
    font-weight: 600;
    font-size: 17px;
    color: var(--brand-blue);
    letter-spacing: 0.3px;
  }

  .holder { position: absolute; left: 30px; top: 168px; }
  .holder__name {
    font-family: "Cinzel", serif;
    font-weight: 400;
    font-size: 19px;
    color: var(--brand-blue);
    letter-spacing: 0.5px;
    white-space: nowrap;
  }
  .holder__role {
    font-family: "Open Sans", sans-serif;
    font-size: 13px;
    color: var(--brand-grey);
    text-align: right;
    margin-top: -2px;
  }

  .contact {
    position: absolute;
    right: 30px; bottom: 26px;
    text-align: right;
    color: var(--text-light);
    font-size: 14px;
    line-height: 1.45;
    list-style: none;
    white-space: nowrap;
  }

  .back-layout {
    position: absolute;
    inset: 0;
    display: flex;
    align-items: center;
    justify-content: center;
    gap: 22px;
  }
  .back-layout__dot { width: 64px; height: 64px; border-radius: 50%; background: var(--brand-blue); flex: none; }
  .back-layout__rule { width: 1px; height: 88px; background: var(--text-muted); flex: none; }
  .company-name {
    font-family: "Cinzel", serif;
    font-weight: 400;
    font-size: 21px;
    line-height: 1.12;
    color: var(--text-muted);
    letter-spacing: 0.6px;
  }
</style>
</head>
<body>

  <section class="card card--front" aria-label="Business card front">
    <svg class="card__art" viewBox="0 0 540 309" preserveAspectRatio="none" aria-hidden="true">
      <defs>
        <linearGradient id="frontBlack" x1="0" y1="0" x2="1" y2="1">
          <stop offset="0" stop-color="#3a393d"/>
          <stop offset="0.5" stop-color="#232225"/>
          <stop offset="1" stop-color="#161517"/>
        </linearGradient>
        <linearGradient id="frontBlue" x1="0" y1="1" x2="1" y2="0">
          <stop offset="0" stop-color="#4aa3e0"/>
          <stop offset="1" stop-color="#1a6fb4"/>
        </linearGradient>
      </defs>
      <path d="M0,268 C170,262 400,170 540,-4 L540,40 C410,205 180,292 0,300 Z" fill="url(#frontBlue)"/>
      <path d="M0,291 C180,284 410,200 540,40 L540,309 L0,309 Z" fill="url(#frontBlack)"/>
      <path d="M420,0 C470,8 510,6 540,0 L540,6 C505,16 465,14 420,0 Z" fill="#1b1a1c"/>
    </svg>

    <div class="brand brand--front">
      <span class="brand__dot"></span>
      <span class="brand__name">Holloway Meridian</span>
    </div>

    <div class="holder">
      <p class="holder__name">Nathan Ashcombe</p>
      <p class="holder__role">Director</p>
    </div>

    <ul class="contact">
      <li>555.014.2290</li>
      <li>nathan@hollowaymeridian.com</li>
      <li>www.hollowaymeridian.com</li>
    </ul>
  </section>

  <section class="card card--back" aria-label="Business card back">
    <div class="back-layout">
      <span class="back-layout__dot"></span>
      <span class="back-layout__rule"></span>
      <p class="company-name">Holloway<br>Meridian<br>Advisory Pty Ltd</p>
    </div>
  </section>

</body>
</html>
```